Meridian Rest Supply Needs Business Card

Looking for a very nice looking business card. Creative but not extravagant. We sell beds and pillows across the U.S. and need something professional but catchy. I have attached the logo.

Name : Dale Fenwick
Title : President
Phone : (800) 417-2964
Email: sleep@quorvana.com
Website: www.quorvana.com

Can be single-sided or double-sided
horizontal or vertical

Can use Blues/Greys

Target Market(s)

Mass Market

Industry/Entity Type

Retail

Contact Information for Business Card

Name : Dale Fenwick
Title : President
Phone : (800) 417-2964
Email: sleep@quorvana.com
Website: www.quorvana.com

Requirements
Must have
• Clean, Modern, Smooth
• Can use Blues/Greys
• On the other side without the information - have something simple like www.quorvana.com or our logo
Nice to have
• Surprise me
Should not have
• Nothing crazy, nothing cluttered

```html
<!DOCTYPE html>
<html lang="en">
<head>
<meta charset="UTF-8">
<title>Quorvana – Business Card</title>
<link rel="stylesheet" href="https://fonts.googleapis.com/css2?family=Open+Sans:wght@400&display=swap">
<style>
  :root {
    --sky: #4ad3f7;
    --paper: #ffffff;
    --rule: #b9b9b9;
  }
  * { margin: 0; padding: 0; box-sizing: border-box; }
  html, body { width: 1200px; height: 741px; overflow: hidden; background: var(--paper); }
  .card {
    position: relative;
    width: 1200px;
    height: 741px;
    background: var(--paper);
    overflow: hidden;
    font-family: "Open Sans", Arial, sans-serif;
  }
  .card__wedge { position: absolute; inset: 0; }
  .brand-name {
    position: absolute;
    left: 60px;
    top: 100px;
    font-family: "Open Sans", Arial, sans-serif;
    font-weight: 400;
    font-size: 100px;
    line-height: 1;
    letter-spacing: -1px;
    color: var(--sky);
    white-space: nowrap;
  }
  .divider {
    position: absolute;
    left: 53px;
    top: 239px;
    width: 472px;
    height: 1px;
    background: var(--rule);
  }
  .person {
    position: absolute;
    left: 62px;
    top: 278px;
    font-size: 36px;
    font-weight: 400;
    line-height: 1;
    color: var(--sky);
    text-transform: uppercase;
    letter-spacing: 0.3px;
    white-space: nowrap;
  }
  .contact-list { list-style: none; }
  .contact {
    position: absolute;
    left: 676px;
    display: flex;
    align-items: center;
    height: 58px;
    color: var(--paper);
    font-size: 23px;
    white-space: nowrap;
  }
  .contact--phone { top: 386px; }
  .contact--email { top: 487px; }
  .contact--web   { top: 587px; }
  .contact__icon { width: 58px; height: 58px; flex: none; margin-right: 32px; }
  .contact--email .contact__text,
  .contact--web .contact__text { text-transform: uppercase; }
</style>
</head>
<body>
<main class="card">
  <svg class="card__wedge" width="1200" height="741" viewBox="0 0 1200 741" aria-hidden="true">
    <polygon points="1200,0 1200,741 0,741" fill="var(--sky)"/>
  </svg>

  <div class="brand-name">quorvana</div>
  <div class="divider"></div>
  <p class="person">Dale Fenwick President</p>

  <ul class="contact-list">
    <li class="contact contact--phone">
      <svg class="contact__icon" viewBox="0 0 58 58" aria-hidden="true">
        <circle cx="29" cy="29" r="29" fill="var(--paper)"/>
        <path transform="translate(15.2 15.2) scale(1.15)" fill="var(--sky)" d="M6.62 10.79c1.44 2.83 3.76 5.14 6.59 6.59l2.2-2.2c.27-.27.67-.36 1.02-.24 1.12.37 2.33.57 3.57.57.55 0 1 .45 1 1V20c0 .55-.45 1-1 1-9.39 0-17-7.61-17-17 0-.55.45-1 1-1h3.5c.55 0 1 .45 1 1 0 1.25.2 2.45.57 3.57.11.35.03.74-.25 1.02l-2.2 2.2z"/>
      </svg>
      <span class="contact__text">(800) 417-2964</span>
    </li>
    <li class="contact contact--email">
      <svg class="contact__icon" viewBox="0 0 58 58" aria-hidden="true">
        <circle cx="29" cy="29" r="29" fill="var(--paper)"/>
        <rect x="14" y="19" width="30" height="21" rx="2" fill="var(--sky)"/>
        <polyline points="15,21 29,32 43,21" fill="none" stroke="var(--paper)" stroke-width="2.5"/>
      </svg>
      <span class="contact__text">sleep@quorvana.com</span>
    </li>
    <li class="contact contact--web">
      <svg class="contact__icon" viewBox="0 0 58 58" aria-hidden="true">
        <circle cx="29" cy="29" r="29" fill="var(--paper)"/>
        <rect x="0" y="21" width="58" height="16" fill="var(--sky)"/>
        <text x="29" y="34" text-anchor="middle" font-family="Open Sans, Arial, sans-serif" font-size="15" font-weight="700" fill="var(--paper)">www</text>
      </svg>
      <span class="contact__text">www.quorvana.com</span>
    </li>
  </ul>
</main>
</body>
</html>
```